Collagen Tub Packaging Design for a New Brand

PLEASE DON'T SEND ANY NEW DESIGNS WE JUST HAVE TO DECIDE WITH MY PARTNERS THANKS A LOT.
I've created a very detailed document & design examples of what we like in certain designs and what we don't.

There are 3 documents:
1- Brief for the Design (please read it before designing)
2- Brand Design Examples that we like (and why we like them)
3- Die cut for the packaging design. This will be it's dimensions.

We are NOT looking for someone to micro-manage. In contrast, we want someone to help us express our ideas better with their design. Nothing I say in these briefs are there to limit the creativity of the designer, because if we knew exactly what we wanted we would do it ourselves but we trust the designer's expertise in this packaging design.

In short: We want our brand to feel premium, high-quality & trust worthy with it's design not feeling very busy or bloated. We don't have a logo source file, but you'll get the idea of what we want when you see it).

Let me know if you have any further questions, will answer each question real fast.

Thanks.

Target Market(s)

Pretty much everyone above 25+ in Turkey because nearly all of them are using are collagens so our audience is wild.

Industry/Entity Type

Collagen - Health, Wellness & Supplements

Font styles to use
Serif
Sans Serif

Colors

Designer to choose colors to be used in the design.

Requirements
Must have
• Our design should be distinct, a design style which everyone can identify from 10 meters away if they know the product. This is a MUST have for us. It's up to designer to achieve it. This can be just a simple color palette aswell.
Should not have
• It shouldn't feel bloated and very busy. Please avoid very detailed icons (as a rule of thumb, if you can make it work great)

```html
<!DOCTYPE html>
<html lang="en">
<head>
<meta charset="utf-8">
<title>Novalume Hydrolyzed Collagen Peptides – Label</title>
<link rel="stylesheet" href="https://fonts.googleapis.com/css2?family=Cinzel:wght@500;600&family=Marcellus&family=Alegreya:wght@500&family=Oswald:wght@500&family=Raleway:wght@300;400&display=swap">
<style>
  :root {
    --backdrop: #b7d8f2;
    --navy-deep: #141f6b;
    --navy: #1b2f8f;
    --royal: #2a4ab0;
    --sky-glow: #5f8fc7;
    --silver: #d9dde3;
    --silver-dark: #9ea3aa;
    --ink: #27316b;
    --white: #f4f6fa;
    --cross: #2f6fc8;
  }
  * { margin: 0; padding: 0; box-sizing: border-box; }
  html, body { width: 1200px; height: 1200px; overflow: hidden; }
  body { background: var(--backdrop); position: relative; }

  .label {
    position: absolute; left: 174px; top: 39px;
    width: 853px; height: 1122px; overflow: hidden;
    background: linear-gradient(100deg, var(--sky-glow) 0%, var(--royal) 30%, var(--navy) 60%, var(--navy-deep) 85%, #3a4a8e 100%);
    color: var(--white);
  }
  .label__pattern {
    position: absolute; left: 40px; top: 60px; width: 780px; height: 880px;
    border-radius: 50%;
    background: radial-gradient(circle, rgba(255,255,255,0.06) 0%, rgba(255,255,255,0.03) 50%, rgba(255,255,255,0) 70%);
  }
  .label__rule {
    position: absolute; left: 0; top: 42px; width: 100%; height: 22px;
    background: linear-gradient(180deg, var(--silver) 0%, #ffffff 40%, var(--silver-dark) 100%);
  }
  .center { position: absolute; left: 0; width: 100%; text-align: center; }

  .brand {
    top: 150px; font-family: "Marcellus", serif; font-size: 92px; line-height: 1;
    color: var(--white); letter-spacing: 1px;
  }
  .tagline {
    top: 244px; font-family: "Marcellus", serif; font-size: 32px; line-height: 1;
    color: var(--white); letter-spacing: 1px; padding-left: 90px;
  }
  .product-type {
    position: absolute; left: 95px; top: 338px;
    font-family: "Alegreya", serif; font-weight: 500; font-size: 44px; line-height: 1;
    color: var(--silver);
  }
  .product-name {
    top: 382px; font-family: "Cinzel", serif; font-weight: 600; font-size: 118px; line-height: 1;
    color: var(--silver); letter-spacing: 2px; padding-left: 30px;
  }
  .product-sub {
    top: 500px; font-family: "Cinzel", serif; font-weight: 600; font-size: 52px; line-height: 1;
    color: var(--silver); letter-spacing: 4px; padding-left: 20px;
  }
  .claims {
    position: absolute; left: 90px; top: 605px; width: 682px; height: 58px;
    border-radius: 29px;
    background: linear-gradient(180deg, #f2f3f5 0%, var(--silver) 100%);
    display: flex; align-items: center; justify-content: center; gap: 30px;
    font-family: "Marcellus", serif; font-size: 28px; color: var(--ink);
  }
  .benefits {
    position: absolute; left: 100px; top: 700px; width: 680px;
    display: flex; justify-content: space-between;
    font-family: "Marcellus", serif; font-size: 27px; color: var(--white);
  }
  .cross { position: absolute; left: 21px; top: 736px; }
  .flavour {
    position: absolute; left: 211px; top: 813px; width: 437px; height: 56px;
    border-radius: 28px; border: 1.5px solid #3d63c9;
    background: linear-gradient(90deg, #3a4fa8 0%, #2546b8 100%);
    display: flex; align-items: center; justify-content: center;
    font-family: "Cinzel", serif; font-weight: 600; font-size: 38px; letter-spacing: 2px;
    color: var(--silver);
  }
  .stat { position: absolute; top: 900px; width: 160px; margin-left: -80px; text-align: center; }
  .stat__value {
    font-family: "Oswald", sans-serif; font-weight: 500; font-size: 62px; line-height: 1;
    color: var(--silver);
  }
  .stat__value small { font-size: 30px; }
  .stat__label {
    font-family: "Raleway", sans-serif; font-weight: 400; font-size: 24px; line-height: 1;
    color: var(--silver); margin-top: 8px;
  }
  .footer {
    position: absolute; left: 120px; top: 1024px; width: 630px;
    display: flex; justify-content: space-between;
    font-family: "Raleway", sans-serif; font-weight: 300; font-size: 24px; color: var(--silver);
  }
</style>
</head>
<body>
  <main class="label">
    <div class="label__pattern" role="img" aria-label="Faint ornamental mandala pattern across the label"></div>
    <div class="label__rule"></div>

    <div class="center brand">Novalume</div>
    <div class="center tagline">Her gün iyi</div>

    <div class="product-type">hydrolyzed</div>
    <h1 class="center product-name">COLLAGEN</h1>
    <div class="center product-sub">PEPTIDES</div>

    <div class="claims"><span>HIGH ABSORPTION</span><span>|</span><span>HIGH-QUALITY MATERIAL</span></div>

    <div class="benefits">
      <span>SKIN</span><span>|</span><span>HAIR</span><span>|</span><span>JOINT</span><span>|</span><span>MOOD</span><span>|</span><span>FAT LOSS</span>
    </div>

    <svg class="cross" width="122" height="193" viewBox="0 0 122 193" aria-hidden="true">
      <path d="M29 0h43v66h50v67H72v60H29v-60H0V66h29z" fill="var(--cross)" opacity="0.8"/>
    </svg>

    <div class="flavour">FLAVOURLESS</div>

    <div class="stat" style="left:162px"><div class="stat__value">0<small>G</small></div><div class="stat__label">SUGAR</div></div>
    <div class="stat" style="left:282px"><div class="stat__value">0<small>G</small></div><div class="stat__label">CARBS</div></div>
    <div class="stat" style="left:391px"><div class="stat__value">0<small>G</small></div><div class="stat__label">FAT</div></div>
    <div class="stat" style="left:518px"><div class="stat__value">11<small>G</small></div><div class="stat__label">PROTEIN</div></div>
    <div class="stat" style="left:685px"><div class="stat__value">12<small>G</small></div><div class="stat__label">COLLAGEN</div></div>

    <div class="footer"><span>DIETARY SUPPLEMENT</span><span>|</span><span>NET WT 21.87 OZ (620g)</span></div>
  </main>
</body>
</html>
```